Design für satanierte Visitenkarten (transparent)
Zielgruppe
Wir sind ein Online Bildportal, bei dem man wie z. B. Pixanda, Lumoraframes und Brightcrate Bilder hochladen und verkaufen kann.
Unterschied zu den o. g. Portalen ist, dass wir uns auf den Exklusivmarkt fokusieren und der Künstler mind. 50% des Umsatzes erhält. Wichtig ist uns, dass sowohl der Kunde als auch der Fotograf/Grafiker Gewinner bei dem Handel sind (Win-Win-Situation)
Unsere Zeilgruppen:
Anbieter: Fotografen, Hobbyfotografen und Grafiker
Kunden: Marketingfirmen jeglicher Art
Aufgabenstellung
Wir benötigen ein Visitenkarten-Design, welches auf satinierte PVC-Visitenkarten (transparent) mit abgerundeten Ecken aufgedruckt wird. In der Design-Datei müssen sämtliche Variablen wie Name, Tel. etc. durch kurzes anklicken und reinschreiben austauschbar sein.
Unser Logo muss miteingebunden werden und sollte schön groß zu erkennen sein. Sollten dennoch Ideen aufkommen, bei denen dies etwas anders aussieht, lassen wir uns gerne überraschen.
Da das Ganze auf transparente Visitenkarten kommt, möchten wir, dass der Hintergrund beim Logo frei bleibt. Ein farbiger Hintergrund bei den Infos ist ok. Ein Hintergrund mit dem Farbcode #ededed wäre sehr passend, da sich auf der Webseite ebenfalls ein Balken mit abgerundeten Ecken befindet, welcher diesen Farbcode enthält.
Folgende Infos sollten enthalten sein:
- Name
- Position (Geschäftsführer etc.)
- Adresse
- Tel.
- Fax.
- Email
- Webadresse
Die Visitenkarten werden folgende Maße aufweisen:
Entwurfformat: 9 x 6 cm
Entformat: 8,5 x 5,5 cm
Folgende Punkte müssen laut Pruckerei beachtet werden:
Dateiformat: Das beste Druckergebnis erhalten Sie mit Vorlagen im Vektorformat (.ai und .eps ). Bitte senden Sie uns die Datei mit offenen Ebenen, die Texte in Pfade gewandelt oder gerastert (ansonsten ggf. den Font separat. Dies gilt auch für PDFs, da der Druck mit Illustrator vorbereitet wird!). Die Erstellung einer Stanzform oder eines Prägeklischees ist nur mit Vektordaten möglich.
Farbraum: Senden Sie uns die Daten unbedingt in CMYK (Coated FOGRA27). Die Umwandlung von RGB- in CMYK-Daten kann zu Farbabweichungen führen, daher nehmen Sie die Umwandlung bitte ggf. vor der Einsendung Ihrer Datei selbst vor. Wenn Ihr Design weiße Elemente enthalten soll, können Sie diese in 100% Cyan anlegen. Bitte fügen Sie dann eine Notiz wie "Cyan = Weiß" bei.
Beschnittzugabe: Zur Gestaltung von..

```html
<!DOCTYPE html>
<html lang="de">
<head>
<meta charset="utf-8">
<title>Lumivista Visitenkarte</title>
<link href="https://fonts.googleapis.com/css2?family=Crimson+Pro:wght@400;600;700&display=swap" rel="stylesheet">
<style>
  :root {
    --page-bg: #8a8a8a;
    --card-light: #d2d2d2;
    --card-dark: #bdbdbd;
    --ink: #2a2522;
    --brand: #a8446e;
    --rule: #2a2522;
  }
  html, body {
    margin: 0;
    width: 1200px;
    height: 1200px;
    overflow: hidden;
    background: var(--page-bg);
  }
  .card {
    position: absolute;
    left: 296px;
    top: 200px;
    width: 618px;
    height: 400px;
    border-radius: 26px;
    background: linear-gradient(160deg, var(--card-light) 0%, #cfcfcf 45%, var(--card-dark) 100%);
    font-family: "Crimson Pro", serif;
    color: var(--ink);
    overflow: hidden;
  }
  .brand {
    position: absolute;
    left: 40px;
    top: 86px;
    display: flex;
    align-items: center;
    gap: 22px;
  }
  .brand-dot {
    width: 62px;
    height: 62px;
    border-radius: 50%;
    background: var(--brand);
  }
  .brand-name {
    font-size: 104px;
    font-weight: 600;
    line-height: 1;
    color: var(--ink);
    letter-spacing: -1px;
  }
  .brand-tagline {
    position: absolute;
    left: 128px;
    top: 178px;
    font-size: 17px;
    font-weight: 700;
    letter-spacing: 11px;
    color: var(--brand);
  }
  .person {
    position: absolute;
    left: 29px;
    top: 234px;
    font-size: 31px;
    line-height: 1;
    white-space: nowrap;
  }
  .person .surname { font-weight: 700; }
  .person .role { font-size: 22px; margin-left: 4px; }
  .person-rule {
    position: absolute;
    left: 2px;
    top: 268px;
    width: 428px;
    height: 1.5px;
    background: var(--rule);
  }
  .contact {
    position: absolute;
    font-size: 21px;
    line-height: 23px;
    white-space: nowrap;
  }
  .contact p { margin: 0; }
  .address { left: 29px; top: 275px; }
  .phones { left: 29px; top: 324px; }
  .online { left: 289px; top: 324px; }
  .online .web { font-weight: 700; }
  .confetti {
    position: absolute;
    left: 453px;
    top: 232px;
    width: 165px;
    height: 160px;
    background: radial-gradient(ellipse at 60% 50%, rgba(230,80,60,0.35), rgba(60,140,210,0.3) 55%, rgba(200,210,40,0) 80%);
  }
</style>
</head>
<body>
  <div class="card">
    <div class="brand">
      <span class="brand-dot"></span>
      <span class="brand-name">Lumivista</span>
    </div>
    <div class="brand-tagline">BILDAGENTUR</div>

    <div class="person">Lukas <span class="surname">Brenner</span> <span class="role">Geschäftsführer</span></div>
    <div class="person-rule"></div>

    <div class="contact address">
      <p>Ahornweg 17</p>
      <p>80469 München</p>
    </div>
    <div class="contact phones">
      <p>Tel. +49 (0)89 5550 1842</p>
      <p>Fax +49 (0)89 5550 1843</p>
    </div>
    <div class="contact online">
      <p>kontakt@lumivista.com</p>
      <p class="web">www.lumivista.com</p>
    </div>

    <div class="confetti" role="img" aria-label="Bunte Dreiecksplitter als Dekoration"></div>
  </div>
</body>
</html>
```